Business Card Design needed - Something Awesome!

Need a business card designed. Company is "Harbor Vane Consulting" we do consulting and also have sales automation technology.
I'm going to use thick stock or metal, something really nice... I was thinking about a QR Code on the back that would just upload my contact info to the persons contact, etc -

This is a Strategy Company with a tech feel. I'm open to ideas but really want this to be nice!

I need a template that should include:

Name | Position or Title
D: 555.203.8146
www.harborvaneconsulting.example

I'm going to attach my contact so you can use that one, I need to get this printed.

Target Market(s)

Small to mid size customers, Entrepreneurs etc.

Industry/Entity Type

Consulting, Tech, Private Equity.

Contact Information for Business Card

Name, Phone, Maybe email, URL

Font styles to use
Sans Serif

Colors

Designer to choose only greyscale colors for use in the design.

Requirements
Must have
• Fresh, Clean, stand out from the crowd - will be on thick stock or metal.
Nice to have
• Clean, simple yet impactful.
Should not have
• Not cartoonish

```html
<!DOCTYPE html>
<html lang="en">
<head>
<meta charset="utf-8">
<title>Harbor Vane Consulting – Business Card</title>
<link rel="stylesheet" href="https://fonts.googleapis.com/css2?family=Carlito:wght@400;700&family=Montserrat:wght@500;600&display=swap">
<style>
  :root {
    --page-bg: #e8e8e8;
    --card-dark: #2a2a2a;
    --card-paper: #efefef;
    --text-light: #e6e6e6;
    --text-muted: #d4d4d4;
    --brand-ink: #2a2a2a;
  }
  * { margin: 0; padding: 0; box-sizing: border-box; }
  html, body {
    width: 1200px;
    height: 900px;
    overflow: hidden;
    background: var(--page-bg);
  }
  .canvas {
    position: relative;
    width: 1200px;
    height: 900px;
  }
  .business-card {
    position: absolute;
    left: 80px;
    top: 152px;
    width: 1040px;
    height: 595px;
    display: flex;
    box-shadow: 0 6px 18px rgba(0, 0, 0, 0.18);
  }
  .contact-side {
    position: relative;
    width: 540px;
    height: 100%;
    background: var(--card-dark);
    color: var(--text-light);
    padding: 66px 29px 0 29px;
  }
  .holder-name {
    font-family: "Montserrat", sans-serif;
    font-weight: 600;
    font-size: 40px;
    line-height: 1.1;
  }
  .holder-title {
    font-family: "Montserrat", sans-serif;
    font-weight: 500;
    font-size: 24px;
    line-height: 1.2;
    color: var(--text-muted);
    margin-top: 2px;
    margin-left: 3px;
  }
  .address-block,
  .details-block {
    position: absolute;
    left: 29px;
    font-family: "Carlito", sans-serif;
    font-style: normal;
    font-size: 25px;
    line-height: 36px;
    color: var(--text-muted);
    white-space: nowrap;
  }
  .address-block { top: 302px; }
  .details-block { top: 421px; }
  .brand-side {
    flex: 1;
    height: 100%;
    background: var(--card-paper);
    display: flex;
    align-items: center;
    justify-content: center;
  }
  .brand-name {
    font-family: "Montserrat", sans-serif;
    font-weight: 500;
    font-size: 46px;
    letter-spacing: 2px;
    color: var(--brand-ink);
    white-space: nowrap;
  }
</style>
</head>
<body>
<main class="canvas">
  <article class="business-card">
    <section class="contact-side">
      <h1 class="holder-name">Daniel R. Ashford</h1>
      <p class="holder-title">Founder / CEO</p>
      <address class="address-block">
        48/210 Quay Lane.<br>
        United Kingdom
      </address>
      <div class="details-block">
        <p>Mob : 555.203.8146</p>
        <p>Email : emailaddresshere</p>
        <p>Web : www.harborvaneconsulting.example</p>
      </div>
    </section>
    <section class="brand-side">
      <p class="brand-name">HARBOR VANE</p>
    </section>
  </article>
</main>
</body>
</html>
```